Professional Services/Construction Management (Millwork) Biz Cards

We've decided on a logo and have our color palette set, now we want to design some very professional looking cards that make a strong first impression - they'll reflect our tagline (that we're going to put on the back: Innovative. Professional. Leaders.

The example business card shows generally the direction we've been thinking of going for the back side - **but we're open to other ideas**

Target Market(s)

The cards should target more high-end (wealthy) owners and general contracting companies. We want them to convey a strong first impression - in a professional and not garish way.

Industry/Entity Type

Construction Company

Contact Information for Business Card

There needs to be a place for our company contractor's license number and business address. We want to also have people's names, titles, phone number, email address. The back can be the logo, tagline and web address

Requirements
Must have
• follow our color palette
Nice to have
• Font & Styles should compliment the Harrow Joinery fonts, but not necessarily match exactly

```html
<!DOCTYPE html>
<html lang="en">
<head>
<meta charset="utf-8">
<title>Harrow Joinery Business Cards</title>
<link rel="stylesheet" href="https://fonts.googleapis.com/css2?family=Open+Sans:wght@400;600;700;800&display=swap">
<style>
  :root {
    --stage: #2a2a2c;
    --charcoal-light: #4a4a4d;
    --charcoal-dark: #343436;
    --green: #5b9e44;
    --paper: #f3f3f3;
    --white: #ffffff;
    --brown: #5c4c40;
    --steel: #8e9196;
    --steel-ring: #6d6f73;
    --soft-text: #d6d6d6;
  }
  * { box-sizing: border-box; margin: 0; padding: 0; }
  html, body {
    width: 1200px; height: 900px; overflow: hidden;
    background: var(--stage);
    font-family: "Open Sans", Arial, sans-serif;
  }
  .canvas {
    position: relative; width: 1200px; height: 900px;
    display: flex; flex-direction: column; align-items: center; justify-content: center; gap: 60px;
  }
  .card {
    position: relative; width: 560px; height: 320px;
    border-radius: 18px; overflow: hidden;
    box-shadow: 0 10px 30px rgba(0,0,0,.45);
  }

  /* Back of card */
  .card-back {
    background: linear-gradient(160deg, var(--charcoal-light), var(--charcoal-dark));
  }
  .card-back .tag-band {
    position: absolute; left: 0; right: 0; top: 112px; height: 82px;
    background: var(--green);
  }
  .card-back .mark {
    position: absolute; left: 28px; top: 78px; width: 150px; height: 150px;
    border-radius: 50%; background: var(--brown);
    border: 6px solid var(--charcoal-dark);
    display: flex; align-items: center; justify-content: center; text-align: center;
  }
  .card-back .mark-name {
    color: var(--white); font-weight: 700; font-size: 19px; line-height: 1.15;
  }
  .card-back .tagline {
    position: absolute; left: 200px; top: 139px;
    color: var(--white); font-weight: 700; font-size: 20px; white-space: nowrap;
  }
  .card-back .web {
    position: absolute; left: 205px; top: 208px;
    display: flex; align-items: center; gap: 12px;
    color: var(--green); font-size: 13px;
  }
  .card-back .web-rule { width: 190px; height: 1px; background: var(--green); }

  /* Front of card */
  .card-front { background: var(--paper); }
  .card-front .info-panel {
    position: absolute; left: 0; right: 0; top: 140px; height: 146px;
    background: linear-gradient(180deg, var(--charcoal-light), var(--charcoal-dark));
  }
  .card-front .rule {
    position: absolute; left: 0; right: 0; top: 286px; height: 4px; background: var(--white);
  }
  .card-front .foot-band {
    position: absolute; left: 0; right: 0; top: 290px; bottom: 0; background: var(--green);
  }
  .card-front .mark {
    position: absolute; left: 30px; top: 14px; width: 120px; height: 120px;
    border-radius: 50%; background: var(--steel);
    border: 4px solid var(--steel-ring);
    display: flex; align-items: center; justify-content: center; text-align: center;
  }
  .card-front .mark-name {
    color: var(--white); font-weight: 700; font-size: 15px; line-height: 1.15;
  }
  .card-front .person {
    position: absolute; right: 34px; top: 152px; text-align: right;
  }
  .card-front .person-name {
    color: var(--white); font-weight: 700; font-size: 20px; line-height: 1.1;
  }
  .card-front .person-title { color: var(--soft-text); font-size: 13px; }
  .card-front .contacts {
    position: absolute; left: 30px; top: 178px; list-style: none;
    color: var(--white); font-size: 14px;
  }
  .card-front .contacts li { display: flex; align-items: flex-start; gap: 12px; margin-bottom: 7px; line-height: 1.25; }
  .card-front .contacts li:last-child { margin-bottom: 0; }
  .card-front .contacts svg { flex: none; width: 18px; height: 18px; }
</style>
</head>
<body>
<main class="canvas">

  <section class="card card-back" aria-label="Business card back">
    <div class="tag-band"></div>
    <div class="mark"><span class="mark-name">Harrow<br>Joinery</span></div>
    <p class="tagline">Innovative. Professional. Leaders</p>
    <p class="web"><span>www.yourweb.com</span><span class="web-rule"></span></p>
  </section>

  <section class="card card-front" aria-label="Business card front">
    <div class="info-panel"></div>
    <div class="rule"></div>
    <div class="foot-band"></div>
    <div class="mark"><span class="mark-name">Harrow<br>Joinery</span></div>
    <div class="person">
      <p class="person-name">YOUR NAME</p>
      <p class="person-title">Title</p>
    </div>
    <ul class="contacts">
      <li>
        <svg viewBox="0 0 20 20" aria-hidden="true"><circle cx="10" cy="10" r="8.5" fill="none" stroke="#5b9e44" stroke-width="1.6"/><path d="M7 5.5l1.6 2.2-1 1.1a6 6 0 0 0 3.6 3.6l1.1-1 2.2 1.6-.9 1.5c-3.5.2-7.8-4.1-7.6-7.6z" fill="#5b9e44"/></svg>
        <span>555 010 1234</span>
      </li>
      <li>
        <svg viewBox="0 0 20 20" aria-hidden="true"><rect x="2" y="4.5" width="16" height="11" fill="none" stroke="#5b9e44" stroke-width="1.5"/><path d="M2 4.5l8 6.5 8-6.5" fill="none" stroke="#5b9e44" stroke-width="1.5"/></svg>
        <span>name@yourweb.com</span>
      </li>
      <li>
        <svg viewBox="0 0 20 20" aria-hidden="true"><path d="M10 1.5a5.8 5.8 0 0 0-5.8 5.8c0 4.3 5.8 11.2 5.8 11.2s5.8-6.9 5.8-11.2A5.8 5.8 0 0 0 10 1.5z" fill="#5b9e44"/><circle cx="10" cy="7.3" r="2.2" fill="#3f3f42"/></svg>
        <span>Your Address<br>in Two Line</span>
      </li>
    </ul>
  </section>

</main>
</body>
</html>
```